VORN - Business cards

Business card to be created for Commercial sales staff

Target Market(s)

Commercial businesses

Industry/Entity Type

Commercial

Contact Information for Business Card

Look professional. For commercial clients

Colors
ffffff

Requirements
Must have
• - Vorn Logo
• - Commercial sales staff as postion
• - room for commerical sales manager role
• - person name and their mobile number
• - Website : vornelectrical.com.au
Nice to have
• White background.
• On back of business card just have the logo no other information
Should not have
• Should only have white background on front of card.

```html
<!DOCTYPE html>
<html lang="en">
<head>
<meta charset="UTF-8">
<title>VORN – Business Cards</title>
<link href="https://fonts.googleapis.com/css2?family=Roboto:wght@400;500;900&display=swap" rel="stylesheet">
<style>
  :root {
    --stage: #1c1c1e;
    --paper: #ffffff;
    --ink: #2b2d3a;
    --ink-soft: #3a3a3a;
    --rule: #5a5a5a;
    --brand-red: #c8202a;
    --navy: #262837;
  }
  * { box-sizing: border-box; margin: 0; padding: 0; }
  html, body {
    width: 1200px; height: 800px; overflow: hidden;
    background: var(--stage);
    font-family: "Roboto", Arial, sans-serif;
  }
  .stage {
    position: relative; width: 1200px; height: 800px;
  }
  .card {
    position: absolute; top: 252px;
    width: 520px; height: 297px;
    border-radius: 3px;
    box-shadow: 0 18px 40px rgba(0,0,0,.55);
    overflow: hidden;
  }
  /* Front */
  .card-front { left: 50px; background: var(--paper); }
  .brand {
    position: absolute; left: 190px; top: 58px;
    display: flex; align-items: center; gap: 12px;
  }
  .brand-dot {
    width: 22px; height: 22px; border-radius: 50%;
    background: var(--brand-red);
  }
  .brand-name {
    font-weight: 900; font-size: 62px; letter-spacing: 2px;
    color: var(--ink); line-height: 1;
  }
  .rule-top {
    position: absolute; left: 28px; right: 28px; top: 140px;
    height: 1px; background: var(--rule);
  }
  .person { position: absolute; left: 28px; top: 152px; }
  .person-name { font-size: 20px; font-weight: 500; color: var(--ink-soft); }
  .person-role { font-size: 12px; color: var(--brand-red); margin-top: 2px; }
  .rule-contact {
    position: absolute; left: 300px; right: 28px; top: 212px;
    height: 1px; background: var(--rule);
  }
  .contact {
    position: absolute; right: 28px; top: 222px;
    list-style: none; text-align: right;
    font-size: 12.5px; color: var(--ink-soft); line-height: 19px;
  }
  .contact li { display: flex; justify-content: flex-end; align-items: center; gap: 8px; }
  .contact svg { width: 11px; height: 11px; fill: var(--brand-red); }
  /* Back */
  .card-back {
    left: 630px;
    background: linear-gradient(35deg, var(--navy) 0%, var(--navy) 35%, #6a2a30 60%, var(--brand-red) 100%);
    display: flex; align-items: center; justify-content: center;
  }
  .card-back .brand-name { color: var(--paper); font-size: 72px; }
</style>
</head>
<body>
<main class="stage">
  <section class="card card-front" aria-label="Business card front">
    <div class="brand">
      <span class="brand-dot"></span>
      <span class="brand-name">VORN</span>
    </div>
    <div class="rule-top"></div>
    <div class="person">
      <p class="person-name">Liam Carter</p>
      <p class="person-role">Commercial sales manager</p>
    </div>
    <div class="rule-contact"></div>
    <ul class="contact">
      <li>555 010 2468
        <svg viewBox="0 0 24 24"><path d="M6.6 10.8a15 15 0 0 0 6.6 6.6l2.2-2.2a1 1 0 0 1 1-.25 11.4 11.4 0 0 0 3.6.57 1 1 0 0 1 1 1V20a1 1 0 0 1-1 1A17 17 0 0 1 3 4a1 1 0 0 1 1-1h3.5a1 1 0 0 1 1 1c0 1.25.2 2.45.57 3.57a1 1 0 0 1-.25 1z"/></svg>
      </li>
      <li>sales@vornmail.com
        <svg viewBox="0 0 24 24"><path d="M2 5h20v14H2z M3.5 6.5 12 12.5l8.5-6v-.01H3.5z" fill-rule="evenodd"/></svg>
      </li>
      <li>www.vornelectrical.com.au
        <svg viewBox="0 0 24 24"><path d="M2 4h20v13H14v2h3v2H7v-2h3v-2H2zm2 2v9h16V6z"/></svg>
      </li>
    </ul>
  </section>

  <section class="card card-back" aria-label="Business card back">
    <span class="brand-name">VORN</span>
  </section>
</main>
</body>
</html>
```